Social Media Monitoring Web Site Design

We need a responsive web design for a new company based in Ireland. We offer a social media monitoring service that works in a call centre environment. Our service name is 'VANTO'. We have a logo that is attached.

Sites we like (in no particular order):

1. http://www.plumvector.com/
2. https://taldrix.io/
3. https://www.loomhaven.com/

We want the web site to have the following sections:

HOME
VANTO PLATFORM
VANTO SERVICE
CASE STUDIES
ABOUT US
CONTACT US

We also need a customer Login link. The site must be a responsive design.

Target Market(s)

Corporate Customers

Industry/Entity Type

It Company

Coding

Coded - Design and coding required

Number of Pages Required

2 page

Requirements
Must have
• Responsive Design
• Bootstrap
Nice to have
• Animations

```html
<!DOCTYPE html>
<html lang="en">
<head>
<meta charset="utf-8">
<title>VANTO — Social Media Monitoring</title>
<link href="https://fonts.googleapis.com/css2?family=Lato:wght@300;400&display=swap" rel="stylesheet">
<style>
  :root {
    --orange: #e8781f;
    --blue: #1896d3;
    --text-dark: #3a3a3a;
    --text-grey: #555555;
    --caption-grey: #4a4a4a;
    --white: #ffffff;
    --black: #000000;
    --brand-gradient: linear-gradient(90deg, var(--orange) 0%, #8a8a76 50%, var(--blue) 100%);
  }
  * { box-sizing: border-box; margin: 0; padding: 0; }
  html, body {
    width: 1200px; height: 1040px; overflow: hidden;
    background: var(--white);
    font-family: "Lato", Arial, sans-serif;
  }
  .page { position: relative; width: 1200px; height: 1040px; }

  .top-strip { position: absolute; top: 0; left: 0; width: 100%; height: 12px; background: var(--brand-gradient); }
  .login-link {
    position: absolute; top: 12px; right: 0; width: 212px; height: 35px;
    background: var(--blue); color: var(--white); text-decoration: none;
    font-size: 19px; line-height: 35px; text-align: center;
  }

  .brand {
    position: absolute; left: 40px; top: 86px;
    display: flex; align-items: center; gap: 12px;
    color: var(--text-dark); font-size: 40px; font-weight: 400; letter-spacing: 2px;
  }
  .brand-mark { width: 30px; height: 30px; background: var(--blue); }

  .main-nav { position: absolute; top: 92px; right: 38px; display: flex; gap: 0; }
  .main-nav a {
    position: relative; display: block; padding: 0 14px;
    color: var(--text-dark); text-decoration: none; font-size: 16px; line-height: 24px;
  }
  .main-nav a.is-active::after {
    content: ""; position: absolute; left: 0; right: 0; bottom: -12px; height: 3px;
    background: var(--brand-gradient);
  }

  .hero {
    position: absolute; top: 190px; left: 0; width: 100%; height: 519px;
    background: linear-gradient(120deg, #c9a58a 0%, #7fb6d6 35%, #d98f84 60%, #9bc3de 85%, #d4b26e 100%);
  }
  .hero-caption {
    position: absolute; left: 73px; top: 190px; width: 1054px; height: 165px;
    background: rgba(255,255,255,0.72);
    display: flex; align-items: center; justify-content: center;
    text-align: center; color: var(--caption-grey);
    font-weight: 300; font-size: 50px; line-height: 62px; letter-spacing: 1px;
  }

  .cta-band {
    position: absolute; top: 709px; left: 0; width: 100%; height: 45px;
    background: var(--brand-gradient);
  }
  .cta-band a {
    position: absolute; top: 0; line-height: 45px;
    color: var(--white); text-decoration: none; font-size: 20px; letter-spacing: 0.5px;
  }
  .cta-consult { left: 330px; }
  .cta-demo { left: 672px; }
  .scroll-button { position: absolute; left: 562px; top: 688px; width: 90px; height: 90px; }

  .intro {
    position: absolute; top: 831px; left: 168px; width: 864px;
    text-align: center; color: var(--text-grey); font-size: 19px; line-height: 25px;
  }
</style>
</head>
<body>
<div class="page">
  <div class="top-strip"></div>
  <a class="login-link" href="#">login / Signup</a>

  <header>
    <div class="brand"><span class="brand-mark"></span><span class="brand-name">VANTO</span></div>
    <nav class="main-nav">
      <a class="is-active" href="#">HOME</a>
      <a href="#">VANTO PLATFORM</a>
      <a href="#">VANTO SERVICE</a>
      <a href="#">CASE STUDIES</a>
      <a href="#">ABOUT US</a>
      <a href="#">CONTACT US</a>
    </nav>
  </header>

  <section class="hero" role="img" aria-label="Photo of a diverse crowd of smiling people holding up tablets showing portraits">
    <p class="hero-caption">Neque porro quisquam est qui dolorem<br>amet, consectetur, adipisc.</p>
  </section>

  <div class="cta-band">
    <a class="cta-consult" href="#">FREE CONSULTATION</a>
    <a class="cta-demo" href="#">TRY OUR FREE DEMO</a>
  </div>
  <svg class="scroll-button" viewBox="0 0 90 90" aria-label="Scroll down">
    <circle cx="45" cy="45" r="45" fill="var(--black)"/>
    <polyline points="32,32 45,58 58,32" fill="none" stroke="var(--white)" stroke-width="2"/>
  </svg>

  <p class="intro">Maecenas ut eros risus. Cras sodales lectus ut mi molestie interdum in eget nisi. Vestibulum pulvinar justo egestas sem posuere bibendum. Pellentesque fermentum velit tincidunt, lobortis nibh at, vehicula eros. Suspendisse potenti. Mauris posuere, nulla id tempor vehicula, libero metus eleifend ipsum, vitae vestibulum dui tortor ut diam. Maece.</p>
</div>
</body>
</html>
```